Professional BBQ Cleaning Flyer (Before & After Focus)

We need a clean, professional double-sided A5 flyer for a BBQ cleaning business.
This flyer will be handed directly to:
Property managers
Retirement villages
Over 50s communities
Resorts / body corporate
The design must feel professional, trustworthy, and easy to read β not cluttered or cheap.
π― Goal
Use a strong before & after BBQ image to show the value of the service, and position the business as reliable for communal BBQ cleaning.
π Size & Format
A5 (148 x 210mm)
Portrait (vertical)
Double-sided
Print-ready (with bleed)
π¨ Style & Branding
Colours: Red, Black, White
Clean, modern, minimal
Strong, easy-to-read fonts (important for older audience)
Plenty of white space
No emojis, no clutter, no cheap design elements
π₯ FRONT SIDE (IMPORTANT β MAIN FOCUS)
Must include:
Headline:
Professional BBQ Cleaning
For Shared & Communal Areas
Subheadline:
Keep your BBQs clean, safe, and ready for residents & guests
Main Visual :
Side-by-side BEFORE & AFTER BBQ
This is the main focus of the flyer
Must be realistic and high quality
Labels under images:
BEFORE β Greasy β’ Dirty β’ Unsafe
AFTER β Clean β’ Hygienic β’ Ready to Use
Short Bullet Points:
Deep clean of grills, burners & internal components
Ideal for retirement villages, resorts & body corporate
Multiple BBQs cleaned in one visit
Trust Line:
Fully insured & police checked
Call to Action (bottom):
Get a Quote or Book a Service
0438 254 091
www.grillshinecrew.com.au
β¬ BACK SIDE (CREDIBILITY & DETAIL)
Headline:
Trusted by Property Managers & Facilities Teams
Whatβs Included:
Full dismantle and deep clean
Removal of grease, carbon & built-up residue
Grills, burners, trays & surfaces cleaned
Reassembled and checked
Why Choose Us:
Professional, reliable service
Works around your schedule
Ideal for high-use communal BBQ areas
One-off or ongoing maintenance
Ideal For:
Retirement villages
Apartment complexes
Resorts
Body corporate properties
Closing Line:
Keep your shared BBQ areas clean, safe, and presentable year-round
Contact:
Grill Shine Crew
0438 254 091
www.grillshinecrew.com.au
grillshinecrew@mailbox-demo.com.au

```html
<!DOCTYPE html>
<html lang="en">
<head>
<meta charset="utf-8">
<title>Grill Shine Crew – Flyer Back</title>
<link href="https://fonts.googleapis.com/css2?family=Poppins:wght@400;500;600;700;800&display=swap" rel="stylesheet">
<style>
  :root {
    --red: #d7373c;
    --black: #111111;
    --ink: #1d1d1d;
    --white: #ffffff;
    --rule: #cfcfcf;
  }
  * { box-sizing: border-box; margin: 0; padding: 0; }
  html, body { width: 847px; height: 1200px; overflow: hidden; background: var(--white); }
  body { font-family: "Poppins", Arial, sans-serif; color: var(--ink); }
  .flyer { position: relative; width: 847px; height: 1200px; overflow: hidden; background: var(--white); }

  /* Header band */
  .hero { position: absolute; left: 0; top: 0; width: 847px; height: 396px; background: var(--red); color: var(--white); }
  .hero__title { position: absolute; left: 42px; top: 26px; font-size: 43px; line-height: 48px; font-weight: 700; letter-spacing: -0.3px; }
  .hero__label { position: absolute; left: 42px; top: 204px; font-size: 19px; font-weight: 600; letter-spacing: 0.4px; }
  .hero__art { position: absolute; left: 580px; top: 18px; width: 200px; height: 200px; }
  .included { position: absolute; left: 42px; top: 242px; list-style: none; }
  .included li { display: flex; align-items: flex-start; gap: 12px; font-size: 21px; line-height: 30px; font-weight: 500; margin-bottom: 4px; }
  .included svg { flex: 0 0 22px; margin-top: 4px; }

  /* Why choose us */
  .why { position: absolute; left: 42px; top: 478px; }
  .why__label { font-size: 23px; font-weight: 700; color: var(--black); letter-spacing: 0.3px; margin-bottom: 12px; }
  .why__list { list-style: none; }
  .why__list li { display: flex; align-items: center; gap: 14px; font-size: 24px; line-height: 30px; font-weight: 500; margin-bottom: 7px; }
  .why__list svg { flex: 0 0 26px; }

  /* Ideal for */
  .ideal { position: absolute; left: 42px; top: 766px; width: 763px; }
  .ideal__tab { display: inline-block; background: var(--black); color: var(--white); font-size: 24px; font-weight: 700; padding: 4px 22px 4px 14px; height: 40px; }
  .ideal__grid { display: grid; grid-template-columns: 186px 196px 150px 1fr; border: 2px solid var(--rule); height: 104px; }
  .ideal__cell { padding: 12px 14px; font-size: 21px; line-height: 28px; font-weight: 500; border-right: 2px solid var(--rule); }
  .ideal__cell:last-child { border-right: none; }

  /* Footer */
  .footer { position: absolute; left: 0; top: 934px; width: 847px; height: 266px; background: var(--black); color: var(--white); }
  .footer__line { position: absolute; left: 42px; top: 24px; width: 600px; font-size: 24px; line-height: 33px; font-weight: 500; }
  .brand { position: absolute; left: 42px; top: 152px; width: 260px; display: flex; align-items: center; gap: 12px; }
  .brand__dot { width: 22px; height: 22px; border-radius: 50%; background: var(--red); flex: 0 0 22px; }
  .brand__name { font-size: 26px; font-weight: 700; color: var(--white); line-height: 30px; }
  .contact { position: absolute; left: 345px; top: 112px; width: 460px; }
  .contact__phone { font-size: 60px; font-weight: 700; line-height: 68px; letter-spacing: 0.5px; }
  .contact__web, .contact__email { font-size: 21px; font-weight: 500; color: var(--red); line-height: 29px; white-space: nowrap; }
</style>
</head>
<body>
<main class="flyer">
  <section class="hero">
    <h1 class="hero__title">Trusted by<br>Property Managers<br>&amp; Facilities Teams</h1>
    <svg class="hero__art" role="img" aria-label="Brand illustration: droplet with barbecue grill" viewBox="0 0 200 200">
      <defs>
        <radialGradient id="artGlow" cx="50%" cy="55%" r="55%">
          <stop offset="0" stop-color="#e25a5e"/>
          <stop offset="1" stop-color="#d7373c"/>
        </radialGradient>
      </defs>
      <rect width="200" height="200" rx="20" fill="url(#artGlow)"/>
    </svg>
    <p class="hero__label">WHAT'S INCLUDED</p>
    <ul class="included">
      <li><svg width="22" height="22" viewBox="0 0 22 22"><circle cx="11" cy="11" r="9.5" fill="none" stroke="#fff" stroke-width="2"/><path d="M6.5 11.2l3 3 6-6" fill="none" stroke="#fff" stroke-width="2.2" stroke-linecap="round" stroke-linejoin="round"/></svg>Full dismantle and deep clean</li>
      <li><svg width="22" height="22" viewBox="0 0 22 22"><circle cx="11" cy="11" r="9.5" fill="none" stroke="#fff" stroke-width="2"/><path d="M6.5 11.2l3 3 6-6" fill="none" stroke="#fff" stroke-width="2.2" stroke-linecap="round" stroke-linejoin="round"/></svg>Removal of grease, carbon &amp; built-up residue</li>
      <li><svg width="22" height="22" viewBox="0 0 22 22"><circle cx="11" cy="11" r="9.5" fill="none" stroke="#fff" stroke-width="2"/><path d="M6.5 11.2l3 3 6-6" fill="none" stroke="#fff" stroke-width="2.2" stroke-linecap="round" stroke-linejoin="round"/></svg><span>Grills, burners, trays &amp; surfaces cleaned<br>Reassembled and checked</span></li>
    </ul>
  </section>

  <section class="why">
    <h2 class="why__label">WHY CHOOSE US</h2>
    <ul class="why__list">
      <li><svg width="26" height="26" viewBox="0 0 26 26"><circle cx="13" cy="13" r="13" fill="var(--red)"/><path d="M7.5 13.3l3.6 3.6 7.4-7.4" fill="none" stroke="#fff" stroke-width="2.6" stroke-linecap="round" stroke-linejoin="round"/></svg>Professional, reliable service</li>
      <li><svg width="26" height="26" viewBox="0 0 26 26"><circle cx="13" cy="13" r="13" fill="var(--red)"/><path d="M7.5 13.3l3.6 3.6 7.4-7.4" fill="none" stroke="#fff" stroke-width="2.6" stroke-linecap="round" stroke-linejoin="round"/></svg>Works around your schedule</li>
      <li><svg width="26" height="26" viewBox="0 0 26 26"><circle cx="13" cy="13" r="13" fill="var(--red)"/><path d="M7.5 13.3l3.6 3.6 7.4-7.4" fill="none" stroke="#fff" stroke-width="2.6" stroke-linecap="round" stroke-linejoin="round"/></svg>Ideal for high-use communal BBQ areas</li>
      <li><svg width="26" height="26" viewBox="0 0 26 26"><circle cx="13" cy="13" r="13" fill="var(--red)"/><path d="M7.5 13.3l3.6 3.6 7.4-7.4" fill="none" stroke="#fff" stroke-width="2.6" stroke-linecap="round" stroke-linejoin="round"/></svg>One-off or ongoing maintenance</li>
      <li><svg width="26" height="26" viewBox="0 0 26 26"><circle cx="13" cy="13" r="13" fill="var(--red)"/><path d="M7.5 13.3l3.6 3.6 7.4-7.4" fill="none" stroke="#fff" stroke-width="2.6" stroke-linecap="round" stroke-linejoin="round"/></svg>Fully insured &amp; police checked</li>
    </ul>
  </section>

  <section class="ideal">
    <div class="ideal__tab">Ideal For</div>
    <div class="ideal__grid">
      <div class="ideal__cell">Retirement villages</div>
      <div class="ideal__cell">Apartment complexes</div>
      <div class="ideal__cell">Resorts</div>
      <div class="ideal__cell">Body corporate properties</div>
    </div>
  </section>

  <footer class="footer">
    <p class="footer__line">Keep your shared BBQ areas clean, safe, and presentable year-round</p>
    <div class="brand">
      <span class="brand__dot"></span>
      <span class="brand__name">Grill Shine Crew</span>
    </div>
    <div class="contact">
      <p class="contact__phone">0438 254 091</p>
      <p class="contact__web">www.grillshinecrew.com.au</p>
      <p class="contact__email">grillshinecrew@mailbox-demo.com.au</p>
    </div>
  </footer>
</main>
</body>
</html>
```